Business card design needed

I need a business card that sets my business apart from big gyms and intimidating personal trainers. My personal training business focuses on outdoor and client in-home training, in an environment that is both enjoyable and sustainable for the client.
I train males and females, however a large proportion of my clientelle are female, so I would like the card to lean towards females, but still have a bit of masculine appeal about it.
My business colours are a deep sky blue and lightish red/orange (as seen in logo)

Contact Information for Business Card

Your Vitality Guide
Discover a happier, healthier you!
Benedict Harlow- Health and Fitness Professional
Locations all across the Yarra Valley and Eastern Suburbs of Melbourne
0498315260
benedictharlowpt@quillmail.com.au

Requirements
Must have
• - Mobile number must stand out
- The 'Locations all across the Yarra Valley and Eastern Suburbs of Melbourne' must be clear and easy to read (different colour maybe?)

```html
<!DOCTYPE html>
<html lang="en">
<head>
<meta charset="utf-8">
<title>Your Vitality Guide – Business Card</title>
<link href="https://fonts.googleapis.com/css2?family=Open+Sans:wght@400;600;700&family=Saira:ital,wght@1,600;1,700&display=swap" rel="stylesheet">
<style>
  :root {
    --sky-blue: #1769b0;
    --coral: #d3461f;
    --card-white: #f1f3f5;
    --backdrop: #e4e2de;
    --ink-white: #ffffff;
  }
  * { box-sizing: border-box; margin: 0; padding: 0; }
  html, body { width: 1200px; height: 880px; overflow: hidden; }
  body { background: var(--backdrop); position: relative; font-family: "Open Sans", sans-serif; }

  .card {
    position: absolute;
    width: 560px;
    height: 320px;
    background: var(--card-white);
    overflow: hidden;
    box-shadow: 0 6px 18px rgba(0,0,0,.18);
  }
  .card-art { position: absolute; inset: 0; width: 100%; height: 100%; }

  /* front card */
  .card-front { left: 590px; top: 90px; }
  .brand {
    position: absolute;
    display: flex;
    align-items: center;
    gap: 10px;
  }
  .brand-mark { width: 16px; height: 16px; background: var(--coral); border-radius: 50%; }
  .brand-name {
    font-family: "Open Sans", sans-serif;
    font-weight: 700;
    color: var(--sky-blue);
    letter-spacing: .5px;
  }
  .tagline {
    position: absolute;
    font-family: "Saira", sans-serif;
    font-style: italic;
    font-weight: 600;
    color: var(--coral);
  }
  .card-front .brand { left: 250px; top: 30px; }
  .card-front .brand-name { font-size: 26px; }
  .card-front .tagline { left: 250px; top: 72px; font-size: 17px; }

  .contact { position: absolute; left: 36px; top: 168px; color: var(--ink-white); }
  .contact-name { font-size: 26px; font-weight: 700; line-height: 1.1; }
  .contact-role { font-size: 16px; font-weight: 400; margin-top: 2px; }
  .contact-line { display: flex; align-items: center; gap: 10px; font-size: 16px; margin-top: 6px; }
  .contact-line.phone { font-size: 20px; font-weight: 700; margin-top: 14px; letter-spacing: .5px; }
  .contact-line svg { width: 16px; height: 16px; flex: none; }

  /* back card */
  .card-back { left: 70px; top: 470px; }
  .card-back .brand { left: 40px; top: 58px; }
  .card-back .brand-name { font-size: 30px; }
  .card-back .tagline { left: 40px; top: 104px; font-size: 19px; }
  .locations {
    position: absolute;
    left: 0; top: 194px;
    width: 430px;
    padding: 10px 22px 10px 36px;
    background: var(--coral);
    color: var(--ink-white);
    font-family: "Saira", sans-serif;
    font-style: italic;
    font-weight: 700;
    font-size: 17px;
    line-height: 1.3;
  }
</style>
</head>
<body>

  <section class="card card-front">
    <svg class="card-art" viewBox="0 0 560 320" aria-hidden="true">
      <path d="M0 150 C 140 120, 330 120, 560 170 L560 320 L0 320 Z" fill="var(--sky-blue)"/>
      <path d="M230 118 C 340 120, 460 140, 560 176 L560 186 C 460 156, 340 134, 230 118 Z" fill="var(--coral)"/>
      <path d="M0 0 L190 0 C 150 50, 120 100, 0 140 Z" fill="var(--coral)"/>
      <path d="M190 0 L205 0 C 165 60, 130 110, 0 152 L0 140 C 120 100, 150 50, 190 0 Z" fill="var(--sky-blue)"/>
      <line x1="36" y1="228" x2="340" y2="236" stroke="var(--ink-white)" stroke-width="1" opacity=".5"/>
    </svg>

    <div class="brand">
      <span class="brand-mark"></span>
      <span class="brand-name">Your Vitality Guide</span>
    </div>
    <p class="tagline">Discover a happier, healthier you!</p>

    <div class="contact">
      <h1 class="contact-name">Benedict Harlow</h1>
      <p class="contact-role">Health and Fitness Professional</p>
      <p class="contact-line phone">
        <svg viewBox="0 0 16 16" aria-hidden="true"><rect x="4" y="1" width="8" height="14" rx="1.5" fill="none" stroke="#fff" stroke-width="1.5"/><circle cx="8" cy="12.5" r="1" fill="#fff"/></svg>
        0498.315.260
      </p>
      <p class="contact-line email">
        <svg viewBox="0 0 16 16" aria-hidden="true"><rect x="1" y="3" width="14" height="10" rx="1" fill="none" stroke="#fff" stroke-width="1.5"/><path d="M1.5 3.5 L8 9 L14.5 3.5" fill="none" stroke="#fff" stroke-width="1.5"/></svg>
        benedictharlowpt@quillmail.com.au
      </p>
    </div>
  </section>

  <section class="card card-back">
    <svg class="card-art" viewBox="0 0 560 320" aria-hidden="true">
      <path d="M500 0 C 420 90, 420 230, 500 320 L560 320 L560 0 Z" fill="var(--sky-blue)"/>
      <path d="M516 0 C 440 90, 440 230, 516 320 L560 320 L560 0 Z" fill="var(--coral)"/>
    </svg>

    <div class="brand">
      <span class="brand-mark"></span>
      <span class="brand-name">Your Vitality Guide</span>
    </div>
    <p class="tagline">Discover a happier, healthier you!</p>

    <p class="locations">Locations all across the Yarra Valley<br>and Eastern Suburbs of Melbourne</p>
  </section>

</body>
</html>
```